Government contracting small business needs a web design

Tarrow Ridge Inc is a veteran owned small business that delivers a full range of professional services as well as training in information technology, security and defense intelligence solutions.
We need a professional/corporate looking website where potential clients can view what services are offered.
This being a new company, there is not much that can added more than a narrative statement, stock photos and a place where potential customers and employees can make contact.
Open to ideas.
Target Market(s)
US Government
Industry/Entity Type
Small Business

```html
<!DOCTYPE html>
<html lang="en">
<head>
<meta charset="utf-8">
<title>Tarrow Ridge Inc</title>
<link href="https://fonts.googleapis.com/css2?family=Source+Sans+3:wght@400;600;700&family=PT+Sans+Narrow:wght@700&family=Arimo:wght@400&display=swap" rel="stylesheet">
<style>
:root{
  --ink:#3a3a3a;
  --ink-soft:#4a4a4a;
  --nav:#555;
  --gold-deep:#d9a92a;
  --gold:#f0cf52;
  --gold-light:#f8ec9a;
  --news:#ead56c;
  --panel:#f3f2f3;
  --footer:#5d5d5d;
  --footer-text:#f6e6a2;
  --link:#1f3fbf;
  --frame:#111;
}
*{margin:0;padding:0;box-sizing:border-box}
html,body{width:1200px;height:1080px;overflow:hidden;background:#fff}
body{position:relative;font-family:"Source Sans 3",sans-serif;color:var(--ink)}
.abs{position:absolute}

.site-header{position:absolute;left:0;top:0;width:1200px;height:132px;background:#fff}
.brand{left:132px;top:84px;display:flex;align-items:center;gap:10px;font-weight:700;font-size:26px;color:var(--ink-soft)}
.brand-dot{width:30px;height:30px;border-radius:50%;background:var(--gold-deep)}
.search{left:861px;top:25px;width:210px;height:28px;background:#4d4d4d;border-radius:3px;color:#eee;font-size:14px;padding:6px 11px}
.search svg{position:absolute;right:8px;top:4px}
.main-nav{left:446px;top:86px;display:flex;gap:27px;font-size:18px;color:var(--nav)}
.main-nav span{padding:1px 0}
.main-nav .is-current{background:linear-gradient(#f2f2f2,#cfcfcf);border-radius:6px;padding:1px 9px;box-shadow:0 2px 2px rgba(0,0,0,.25)}

.hero{position:absolute;left:0;top:132px;width:1200px;height:500px;
  background:radial-gradient(ellipse 520px 260px at 600px 340px,#fbf3b4,transparent),linear-gradient(180deg,var(--gold-deep),var(--gold) 55%,var(--gold-light))}
.monitor{position:absolute;background:var(--frame);border:2px solid #e8e8e8;border-radius:8px;box-shadow:0 6px 16px rgba(0,0,0,.3)}
.screen{position:absolute;inset:18px 18px 20px 18px}
.screen-left{background:linear-gradient(135deg,#dfe7ee,#8ea4b8)}
.screen-right{background:linear-gradient(135deg,#666,#2b3d8f 60%,#444)}
.screen-main{background:linear-gradient(120deg,#b9c1c3,#e6eef0 40%,#7c8c8e)}
.hero-title{left:380px;top:212px;font-family:"PT Sans Narrow",sans-serif;font-size:58px;color:#2b2b2b;letter-spacing:-1px}
.hero-copy{left:380px;top:283px;width:457px;height:110px;background:rgba(255,255,255,.55);padding:4px 5px;font-size:17px;line-height:21.5px;color:#333}
.hero-more{left:722px;top:363px;width:110px;height:24px;border-radius:12px;background:linear-gradient(#fff,#cfcfcf);font-size:14px;font-weight:600;text-align:center;line-height:24px;color:#222}
.pager{left:542px;top:594px;display:flex;gap:17px}
.pager i{width:17px;height:17px;border-radius:50%;background:radial-gradient(circle at 40% 35%,#fff,#cfcfcf)}
.pager i.is-active{background:radial-gradient(circle at 40% 35%,#f3d35a,#a87a10)}

.news-bar{position:absolute;left:0;top:632px;width:1200px;height:37px;background:var(--news);border-top:1px solid #fff6c4;border-bottom:1px solid #8a7a3a}
.news-label{left:133px;top:7px;font-size:19px;font-weight:700;color:#1e1e1e}
.news-text{left:309px;top:11px;font-size:13.5px;color:#444}

.content{position:absolute;left:0;top:669px;width:1200px;height:374px;background:linear-gradient(var(--panel),#fff)}
.icon{position:absolute;border-radius:6px}
.feature-title{position:absolute;font-size:16px;font-weight:600;color:#444}
.feature-text{position:absolute;width:200px;font-family:Arimo,sans-serif;font-size:13px;line-height:15.6px;color:#333}
.about-title{left:626px;top:88px;font-size:19px;font-weight:700;color:#555}
.about-text{left:626px;top:122px;width:450px;font-size:13.5px;line-height:18px;text-align:justify;color:#444}
.about-more{left:626px;top:278px;font-family:Arimo,sans-serif;font-size:14px;color:var(--link);text-decoration:underline}

.site-footer{position:absolute;left:0;top:1043px;width:1200px;height:37px;background:var(--footer);color:var(--footer-text);font-size:13.5px}
.copyright{left:121px;top:12px}
.footer-nav{right:123px;top:12px}
</style>
</head>
<body>
<header class="site-header">
  <div class="abs brand"><span class="brand-dot"></span>Tarrow Ridge</div>
  <div class="abs search">Search
    <svg width="26" height="20" viewBox="0 0 26 20"><circle cx="9" cy="8" r="6" fill="none" stroke="#fff" stroke-width="2.5"/><line x1="13" y1="12" x2="22" y2="18" stroke="#fff" stroke-width="4" stroke-linecap="round"/></svg>
  </div>
  <nav class="abs main-nav">
    <span class="is-current">Innovation</span><span>What We Do</span><span>Our Company</span><span>Investors</span><span>Newsroom</span><span>Careers</span>
  </nav>
</header>

<section class="hero">
  <div class="monitor" style="left:135px;top:57px;width:230px;height:264px"><div class="screen screen-left" role="img" aria-label="Globe assembled from puzzle pieces"></div></div>
  <div class="monitor" style="left:835px;top:57px;width:232px;height:264px"><div class="screen screen-right" role="img" aria-label="Blue keyboard key with a padlock symbol"></div></div>
  <div class="monitor" style="left:328px;top:23px;width:548px;height:330px"><div class="screen screen-main" role="img" aria-label="Binary code streaming across a digital surface"></div></div>
</section>
<div class="abs hero-title">IT SECURITY</div>
<div class="abs hero-copy">Lorem ipsum dolor sit amet, consectetur adipiscing elit. Morbi iaculis pretium leo, eu faucibus urna ultricies non. Vestibulum eget augue quam, nec tristique neque.</div>
<div class="abs hero-more">Read More &gt;</div>
<div class="abs pager"><i class="is-active"></i><i></i><i></i><i></i></div>

<div class="news-bar">
  <div class="abs news-label">Latest News &raquo;</div>
  <div class="abs news-text">Lorem ipsum dolor sit amet, consectetur adipiscing elit. Aliquam tincidunt mi id libero egestas ut interdum nibh cursus.</div>
</div>

<main class="content">
  <div class="icon" style="left:124px;top:56px;width:52px;height:52px;background:linear-gradient(#f4f4f4,#bfc8cf)" role="img" aria-label="Report document with magnifying glass icon"></div>
  <div class="feature-title" style="left:180px;top:81px">Analysis</div>
  <p class="feature-text" style="left:132px;top:116px">Lorem ipsum dolor sit amet, consectetur adipiscing elit. Aliquam tincidunt mi id libero egestas ut interdum nibh cursus.</p>

  <div class="icon" style="left:375px;top:56px;width:44px;height:54px;background:linear-gradient(#e23a2a,#6d1d16)" role="img" aria-label="Red target icon"></div>
  <div class="feature-title" style="left:426px;top:81px;font-weight:400">Targeting</div>
  <p class="feature-text" style="left:381px;top:116px;font-size:12px">Lorem ipsum dolor sit amet, consectetur adipiscing elit. Aliquam tincidunt mi id libero egestas ut interdum nibh cursus.</p>

  <div class="icon" style="left:130px;top:198px;width:50px;height:54px;background:linear-gradient(#d8a070,#b53a1f)" role="img" aria-label="Support agent with headset icon"></div>
  <div class="feature-title" style="left:189px;top:223px">Support</div>
  <p class="feature-text" style="left:132px;top:258px">Lorem ipsum dolor sit amet, consectetur adipiscing elit. Aliquam tincidunt mi id libero egestas ut interdum nibh cursus.</p>

  <div class="icon" style="left:382px;top:205px;width:30px;height:46px;background:linear-gradient(#fbe36a,#c99a1c)" role="img" aria-label="Light bulb icon"></div>
  <div class="feature-title" style="left:417px;top:223px">Title Heading</div>
  <p class="feature-text" style="left:381px;top:258px">Lorem ipsum dolor sit amet, consectetur adipiscing elit. Aliquam tincidunt mi id libero egestas ut interdum nibh cursus.</p>

  <h2 class="abs about-title">About the Company</h2>
  <p class="abs about-text">Lorem ipsum dolor sit amet, consectetur adipiscing elit. Aliquam tincidunt mi id libero egestas ut interdum nibh cursus. Nulla erat orci, adipiscing vel molestie ac, vehicula in dui. Proin vel lorem in tellus placerat eleifend. Duis iaculis lorem a ipsum euismod vel ullamcorper arcu placerat. Aenean elementum tortor vel nisi bibendum bibendum. Aliquam fringilla feugiat ante in vestibulum. Sed non justo justo. Aenean et quam dolor. Vivamus aliquet gravida nunc, sed elementum elit blandit vel. Aliquam neque quam, dignissim ac mattis at, hendrerit nec elit. Cras commodo gravida placerat.</p>
  <a class="abs about-more">Read More &gt;</a>
</main>

<footer class="site-footer">
  <div class="abs copyright">&copy; 2012 Tarrow Ridge. All rights reserved.</div>
  <div class="abs footer-nav">Home &nbsp;|&nbsp; Innovation &nbsp;|&nbsp; What We Do &nbsp;|&nbsp; Our Company &nbsp;|&nbsp; Careers &nbsp;|&nbsp; Contact</div>
</footer>
</body>
</html>
```